Business card for accounting firm
Traditional; informative
Project: Business card for accounting firm
Business card for accounting firm - Financial Services
Creative Brief
Professional
J. Dorothy Kessling, MA, MS, MBA
Business Development
418 East Hollister Ave Millbrook, OH 43990 USA
d@pellkessling-tax.example
www.pellkessling-tax.example
Tagline: "Tax Specialists Since 1958"
No sure how to use this. May not be entirely needed.

```html
<!DOCTYPE html>
<html lang="en">
<head>
<meta charset="utf-8">
<title>Pell &amp; Kessling — Business Card</title>
<link rel="stylesheet" href="https://fonts.googleapis.com/css2?family=Libre+Baskerville:wght@400&family=Lato:wght@300;400;700&display=swap">
<style>
  :root {
    --bg: #e9e6e1;
    --card: #ffffff;
    --panel: #e4e4e4;
    --red: #b3262d;
    --ink: #3d3d3d;
    --muted: #6c6c6c;
  }
  * { margin: 0; padding: 0; box-sizing: border-box; }
  html, body { width: 1200px; height: 901px; overflow: hidden; background: var(--bg); }
  .canvas {
    width: 1200px; height: 901px;
    display: flex; flex-direction: column; align-items: center; justify-content: center; gap: 40px;
  }
  .card {
    position: relative; width: 680px; height: 389px; background: var(--card);
    box-shadow: 0 6px 18px rgba(0,0,0,.18); overflow: hidden;
    font-family: "Lato", sans-serif; color: var(--ink);
  }
  .wordmark {
    font-family: "Libre Baskerville", serif; font-weight: 400; color: var(--red);
    font-size: 30px; letter-spacing: 1px; display: flex; align-items: center; gap: 10px; white-space: nowrap;
  }
  .wordmark .mark-square { width: 12px; height: 12px; background: var(--red); }
  .tagline { font-family: "Libre Baskerville", serif; color: var(--muted); font-size: 16px; margin-top: 10px; white-space: nowrap; }

  /* back */
  .back .brand { position: absolute; top: 95px; left: 0; right: 0; display: flex; flex-direction: column; align-items: center; }
  .back .rule { position: absolute; top: 238px; left: 40px; right: 40px; height: 2px; background: var(--red); }
  .back .band {
    position: absolute; top: 272px; left: 0; right: 0; height: 58px; background: var(--red);
    display: flex; align-items: center; justify-content: center;
    color: #fff; font-size: 17px; letter-spacing: 1px;
  }

  /* front */
  .front .brand-area { position: absolute; left: 0; top: 0; width: 300px; height: 100%; }
  .front .top-band { position: absolute; left: 0; top: 120px; width: 300px; height: 26px; background: var(--red); }
  .front .brand { position: absolute; top: 185px; left: 0; width: 300px; display: flex; flex-direction: column; align-items: center; }
  .front .brand .wordmark { font-size: 22px; }
  .front .brand .tagline { font-size: 13px; }
  .front .divider { position: absolute; left: 300px; top: 0; width: 40px; height: 100%; background: var(--red); }
  .front .details { position: absolute; left: 340px; top: 0; right: 0; height: 100%; background: var(--panel); padding: 48px 32px; }
  .person-name { font-family: "Libre Baskerville", serif; font-size: 20px; color: var(--ink); white-space: nowrap; }
  .person-role { font-size: 13px; color: var(--muted); margin-top: 6px; }
  .person-creds { font-size: 11px; color: var(--muted); margin-top: 3px; letter-spacing: .5px; }
  .contact-list { list-style: none; margin-top: 48px; }
  .contact-list li { display: flex; align-items: flex-start; gap: 12px; font-size: 13px; margin-bottom: 12px; line-height: 1.35; }
  .contact-list svg { flex: 0 0 14px; width: 14px; height: 14px; margin-top: 2px; fill: var(--red); }
</style>
</head>
<body>
<main class="canvas">

  <section class="card back" aria-label="Card back">
    <div class="brand">
      <div class="wordmark"><span class="mark-square"></span>Pell &amp; Kessling</div>
      <div class="tagline">Tax Specialists Since 1958</div>
    </div>
    <div class="rule"></div>
    <div class="band">www.pellkessling-tax.example</div>
  </section>

  <section class="card front" aria-label="Card front">
    <div class="brand-area">
      <div class="top-band"></div>
      <div class="brand">
        <div class="wordmark"><span class="mark-square"></span>Pell &amp; Kessling</div>
        <div class="tagline">Tax Specialists Since 1958</div>
      </div>
    </div>
    <div class="divider"></div>
    <div class="details">
      <div class="person-name">J. Dorothy Kessling</div>
      <div class="person-role">Business Development</div>
      <div class="person-creds">MA, MS, MBA</div>
      <ul class="contact-list">
        <li>
          <svg viewBox="0 0 24 24" aria-hidden="true"><path d="M6.6 10.8a15.1 15.1 0 0 0 6.6 6.6l2.2-2.2a1 1 0 0 1 1-.25 11.4 11.4 0 0 0 3.6.57 1 1 0 0 1 1 1V20a1 1 0 0 1-1 1A17 17 0 0 1 3 4a1 1 0 0 1 1-1h3.5a1 1 0 0 1 1 1c0 1.25.2 2.45.57 3.57a1 1 0 0 1-.25 1z"/></svg>
          <span>+1 (614) 555-0142</span>
        </li>
        <li>
          <svg viewBox="0 0 24 24" aria-hidden="true"><path d="M12 2a10 10 0 1 0 0 20 10 10 0 0 0 0-20zm6.9 6h-3a15 15 0 0 0-1.3-3.9A8 8 0 0 1 18.9 8zM12 4c.8 1.2 1.5 2.5 1.9 4h-3.8c.4-1.5 1.1-2.8 1.9-4zM4.3 14a8 8 0 0 1 0-4h3.4a16 16 0 0 0 0 4zm.8 2h3a15 15 0 0 0 1.3 3.9A8 8 0 0 1 5.1 16zm3-8h-3a8 8 0 0 1 4.3-3.9A15 15 0 0 0 8.1 8zM12 20c-.8-1.2-1.5-2.5-1.9-4h3.8c-.4 1.5-1.1 2.8-1.9 4zm2.3-6H9.7a14 14 0 0 1 0-4h4.6a14 14 0 0 1 0 4zm.3 5.9a15 15 0 0 0 1.3-3.9h3a8 8 0 0 1-4.3 3.9zm1.7-5.9a16 16 0 0 0 0-4h3.4a8 8 0 0 1 0 4z"/></svg>
          <span>www.pellkessling-tax.example</span>
        </li>
        <li>
          <svg viewBox="0 0 24 24" aria-hidden="true"><path d="M3 5h18a1 1 0 0 1 1 1v12a1 1 0 0 1-1 1H3a1 1 0 0 1-1-1V6a1 1 0 0 1 1-1zm9 7.2L20 7H4z"/></svg>
          <span>d@pellkessling-tax.example</span>
        </li>
        <li>
          <svg viewBox="0 0 24 24" aria-hidden="true"><path d="M12 2a7 7 0 0 0-7 7c0 5.2 7 13 7 13s7-7.8 7-13a7 7 0 0 0-7-7zm0 9.5A2.5 2.5 0 1 1 12 6.5a2.5 2.5 0 0 1 0 5z"/></svg>
          <span>418 East Hollister Ave<br>Millbrook, OH 43990 USA</span>
        </li>
      </ul>
    </div>
  </section>

</main>
</body>
</html>
```